Name of company is Raven Crest Shear Sharpening and Sales.Card design basic idea; I'm thinking back side just showing a sharp RAVEN CREST. Front side: I'm thinking a tiger showing teeth and claws.With the words "Raven Crest" larger type emphasized on one line.Then "Shear Sharpening and Sales" on the next line.Other info on front of card should be my name and phone #'s and address: Martin Kessling P (555)014-2287 CP (555)017-3365 My address is NOT to be emphasized.Can go at bottom of card. It is: 5072 Henley Court Orlando FL 30417 If all that's too much to fit without looking cluttered than maybe the claw on the front with all the contact info. and just the Tiger on back of card. Whichever looks best.

Target Market(s)

Beauty Salons

Industry/Entity Type

It Company

Contact Information for Business Card

The 2 images,the claw and the tiger,could be either illustrations or photos.Whatever looks best.Got to be eye grabbing either way.

Requirements
Must have
• Contact info. Must be in color. And emphasize the identity. RAVEN CREST.Tiger on one side.Showing TEETH. Raven Crest on the other side. Showing the CLAW. .Both pics must emphasize SHARPNESS...This is a shear SHARPENING business. If one of the claw pics shows cutting grooves into something that's fine too. Card must show sharpness of the claw blade somehow.
Nice to have
• Attention grabbing. Images should jump off the card!
Should not have
• No boring cuddly tiger pics showing no teeth or claws or dull teeth or claws. No Black and whites.. No extra words other than what I've listed.

```html
<!DOCTYPE html>
<html lang="en">
<head>
<meta charset="utf-8">
<title>Raven Crest Shear Sharpening and Sales – Business Card</title>
<link href="https://fonts.googleapis.com/css2?family=Poppins:wght@400;500;600&display=swap" rel="stylesheet">
<style>
  :root {
    --backdrop: #e6e6e8;
    --card-blue: #3451a6;
    --accent-orange: #e3692a;
    --text-white: #ffffff;
    --photo-green: #5f8a4e;
    --photo-amber: #c97a35;
    --photo-rust: #9a5a26;
    --photo-grey: #a7a59e;
    --photo-bark: #8a7a5c;
  }
  * { margin: 0; padding: 0; box-sizing: border-box; }
  html, body {
    width: 1200px;
    height: 900px;
    overflow: hidden;
    background: var(--backdrop);
    font-family: "Poppins", sans-serif;
  }
  .canvas {
    position: relative;
    width: 1200px;
    height: 900px;
  }
  .card {
    position: absolute;
    left: 250px;
    width: 700px;
    height: 400px;
    overflow: hidden;
    box-shadow: 0 10px 28px rgba(0,0,0,0.18);
  }
  .card--photo {
    top: 40px;
    background:
      radial-gradient(ellipse 34% 58% at 50% 62%, rgba(201,122,53,0.95) 0%, rgba(154,90,38,0.75) 45%, rgba(154,90,38,0) 100%),
      radial-gradient(ellipse 30% 40% at 14% 42%, rgba(95,138,78,0.9) 0%, rgba(95,138,78,0) 100%),
      radial-gradient(ellipse 14% 80% at 92% 70%, rgba(138,122,92,0.85) 0%, rgba(138,122,92,0) 100%),
      linear-gradient(180deg, #b8b6ae 0%, var(--photo-grey) 50%, #7e7a6e 100%);
  }
  .card--details {
    top: 460px;
    background: var(--card-blue);
    color: var(--text-white);
  }
  .person {
    position: absolute;
    left: 56px;
    top: 54px;
  }
  .person__name {
    color: var(--accent-orange);
    font-size: 21px;
    font-weight: 500;
    letter-spacing: 2.5px;
    text-transform: uppercase;
    line-height: 1.1;
  }
  .person__role {
    font-size: 17px;
    font-weight: 500;
    letter-spacing: 0.8px;
    line-height: 1.2;
  }
  .brand {
    position: absolute;
    right: 56px;
    top: 132px;
  }
  .brand__name {
    font-size: 36px;
    font-weight: 600;
    letter-spacing: 3px;
    line-height: 1.05;
  }
  .brand__tagline {
    font-size: 13.5px;
    font-weight: 400;
    letter-spacing: 1.3px;
  }
  .contact {
    position: absolute;
    left: 56px;
    top: 262px;
    font-size: 16px;
    letter-spacing: 1.4px;
    line-height: 1.6;
  }
  .contact__line {
    display: flex;
    align-items: center;
    gap: 12px;
  }
  .contact__icon {
    width: 14px;
    height: 16px;
    flex: none;
  }
  .contact__address {
    margin-top: 6px;
    line-height: 1.5;
  }
  .claw-mark {
    position: absolute;
    left: 455px;
    top: 240px;
    width: 170px;
    height: 150px;
    background: radial-gradient(ellipse 50% 50% at 50% 50%, rgba(227,105,42,0.9) 0%, rgba(227,105,42,0.55) 45%, rgba(227,105,42,0) 100%);
  }
</style>
</head>
<body>
  <main class="canvas">
    <section class="card card--photo" role="img" aria-label="Photograph of a snarling tiger baring its sharp teeth"></section>

    <section class="card card--details">
      <div class="person">
        <p class="person__name">Martin Kessling</p>
        <p class="person__role">Founder</p>
      </div>

      <div class="brand">
        <p class="brand__name">RAVEN CREST</p>
        <p class="brand__tagline">Shear Sharpening and Sales</p>
      </div>

      <div class="contact">
        <p class="contact__line">
          <svg class="contact__icon" viewBox="0 0 14 16" aria-hidden="true">
            <path d="M3 1 L5.5 4 L4 6 C5 8.5 6.5 10.5 9 11.5 L10.5 10 L13 12.5 L11 15 C5.5 14 1 8.5 1 3 Z" fill="none" stroke="#fff" stroke-width="1.3" stroke-linejoin="round"/>
          </svg>
          (555)014-2287
        </p>
        <p class="contact__line">
          <svg class="contact__icon" viewBox="0 0 14 16" aria-hidden="true">
            <rect x="3" y="1" width="8" height="14" rx="1.5" fill="none" stroke="#fff" stroke-width="1.3"/>
            <line x1="6" y1="12.5" x2="8" y2="12.5" stroke="#fff" stroke-width="1.3"/>
          </svg>
          (555)017-3365
        </p>
        <p class="contact__address">5072 Henley Court<br>Orlando FL 30417</p>
      </div>

      <div class="claw-mark" role="img" aria-label="Orange claw scratch marks"></div>
    </section>
  </main>
</body>
</html>
```